Pel'k Marrowind Travel

We need a sleek, professional, inviting card to elicit global travel for the experienced and professional traveler. Royal blue, black and silver. (perhaps the wording could be silver with black shadow?-get creative) Maybe a watermark on the front and the full raised logo on the back.
We want a stylish and modern card, but professional.

```html
<!DOCTYPE html>
<html lang="en">
<head>
<meta charset="utf-8">
<title>Pel'k Marrowind Travel – Business Card</title>
<link href="https://fonts.googleapis.com/css2?family=Open+Sans:ital,wght@0,400;0,600;0,700;1,700&display=swap" rel="stylesheet">
<style>
  :root {
    --page: #2b2b2d;
    --card: #1b1b1d;
    --card-edge: #141415;
    --blue: #29a8e0;
    --green: #8cc63f;
    --text: #e4e4e6;
    --muted: #bdbdc2;
  }
  * { margin: 0; padding: 0; box-sizing: border-box; }
  html, body {
    width: 1200px; height: 900px; overflow: hidden;
    background: var(--page);
    font-family: "Open Sans", Arial, sans-serif;
  }
  .canvas {
    position: relative; width: 1200px; height: 900px;
  }
  .card {
    position: absolute; left: 250px; width: 700px; height: 400px;
    background: var(--card);
    box-shadow: 0 14px 30px rgba(0,0,0,.45);
    overflow: hidden;
  }
  .card--front { top: 40px; }
  .card--back { top: 470px; }

  /* front */
  .brand {
    position: absolute; left: 48px; top: 44px;
    display: flex; align-items: center; gap: 12px;
  }
  .brand__dot {
    width: 16px; height: 16px; border-radius: 50%; background: var(--green);
  }
  .brand__name {
    color: var(--blue); font-weight: 700; font-size: 28px; letter-spacing: .5px;
  }
  .divider {
    position: absolute; left: 120px; right: 40px; top: 232px;
    height: 1.5px; background: var(--blue);
  }
  .contact {
    position: absolute; left: 40px; top: 250px;
    list-style: none; color: var(--text); font-size: 17px; line-height: 26px;
  }
  .contact li { display: flex; align-items: center; gap: 10px; }
  .contact svg { width: 14px; height: 14px; fill: var(--green); flex: none; }
  .person {
    position: absolute; right: 52px; top: 152px; text-align: right;
  }
  .person__name {
    color: var(--blue); font-weight: 700; font-size: 26px; text-transform: uppercase; letter-spacing: .3px;
  }
  .person__title { color: var(--text); font-size: 19px; line-height: 24px; }
  .address {
    position: absolute; right: 52px; top: 250px; text-align: right;
    color: var(--text); font-size: 19px; line-height: 26px;
  }
  .band {
    position: absolute; left: 0; right: 0; bottom: 0; height: 9px; background: var(--blue);
  }

  /* back */
  .pattern {
    position: absolute; inset: 0;
    background: linear-gradient(135deg, #222224 0%, #18181a 55%, #202022 100%);
  }
  .back-brand {
    position: absolute; right: 48px; bottom: 46px;
    color: var(--blue); font-weight: 700; font-size: 26px;
  }
</style>
</head>
<body>
<main class="canvas">
  <section class="card card--front" aria-label="Card front">
    <div class="brand">
      <span class="brand__dot"></span>
      <span class="brand__name">Pel'k Marrowind Travel</span>
    </div>

    <div class="person">
      <p class="person__name">Dorian Vell</p>
      <p class="person__title">President</p>
    </div>

    <div class="divider"></div>

    <ul class="contact">
      <li>
        <svg viewBox="0 0 24 24" aria-hidden="true"><path d="M6.6 10.8a15.1 15.1 0 0 0 6.6 6.6l2.2-2.2c.3-.3.7-.4 1-.2 1.1.4 2.3.6 3.6.6.6 0 1 .4 1 1V20c0 .6-.4 1-1 1A17 17 0 0 1 3 4c0-.6.4-1 1-1h3.5c.6 0 1 .4 1 1 0 1.3.2 2.5.6 3.6.1.3 0 .7-.2 1z"/></svg>
        555-310-8824
      </li>
      <li>
        <svg viewBox="0 0 24 24" aria-hidden="true"><path d="M2 5h20v14H2z M2 5l10 8 10-8" /></svg>
        info@pelkmarrowind.com
      </li>
      <li>
        <svg viewBox="0 0 24 24" aria-hidden="true"><circle cx="12" cy="12" r="10"/></svg>
        www.pelkmarrowind.com
      </li>
    </ul>

    <address class="address" style="font-style:normal">
      1870 Harbor Crest Way<br>
      Seacliff CA 90411
    </address>

    <div class="band"></div>
  </section>

  <section class="card card--back" aria-label="Card back">
    <div class="pattern" role="img" aria-label="Tone-on-tone repeated brand pattern background"></div>
    <span class="back-brand">Pel'k Marrowind Travel</span>
  </section>
</main>
</body>
</html>
```